Miel (Honey) Label for Marlow Brook Farm, Temecula Valley, CA

A label design for bottles of freshly harvested natural honey. I've included a picture of the bottles being used. They are 16 oz, plastic bottles. The bee hives are on a farm in Temecula Valley (Wine Country), CA. The name of the farm is Marlow Brook Farm. Marlow Brook Farm specializes in breeding Thoroughbred horses for racing, and equestrian sports of Hunter & Competition Jumping. The owners of the farm are originally from Geneva, Switzerland with their native language being French. I'd like the label to reflect the 3 things - horses, bees/honey, & France. Instead of using the word "honey" on the label, I'd like the word Miel used to include the owners French background. Miel means honey in French. The label should have a Country French look. The words that come to my mind to explain what I'm looking for are: Vintage, Desmond Albright, Linen Loft, Organic, Natural. To include a Fleur de lis somewhere in the design would be a nice representation of the owners French heritage.

The plastic containers being used to package the honey at this time Measures 5-1/4-inch height ( Up and down ) by 3-1/2-inch width
(Across) x 1-3/4-inch thick. I provided a sample picture of the bottle in my images. It's the Greta's Meadow Nectar image I posted on Monday. Please let me know if you have any questions.

Target Market(s)

Natural Food Enthusiasts; Foodies; Millennials; Trendy & hip people from LA coming to the Temecula Valley to go wine tasting. Think Pell Danforth/Venice Beach/ Silverlake, CA. Also, well established, down to earth, sophisticated people with "old" money. Equestrian Sports Enthusiasts of horse racing, English Riding, & Hunter/Jumping. Equestrian Sports are considered and referred to as "the sport of Kings". Farm to table enthusiasts.

Industry/Entity Type

Plastic

Font styles to use
Decorative
Script
Other font styles liked:
• snell Round Bold; Century Gothic; Sans Serif

Colors

Designer to choose colors to be used in the design.

Requirements
Must have
• The name: Marlow Brook Farm somewhere on the label.
• Horses - Silhouettes of thoroughbred horse Hunter Jumping (possibly racing). (See samples of images I pulled from the internet.)
• Bee hives/honey bees/honey
• Honey written in French - Miel
• Country French - Rustic, Simple, but elegant.
Nice to have
• Fleur de lis. Country French & Industrial tone. Trendy & cool with a natural, down to earth feel. A wow factor that draws a person to it.
• Produced in Temecula Valley Wine Country, CA
• Country French/Country Italian/ Romantic/European
Should not have
• Multiple colors. Overly busy. Print too small to read or too ornate to comfortably read.

```html
<!DOCTYPE html>
<html lang="en">
<head>
<meta charset="utf-8">
<title>Miel Label · Marlow Brook Farm</title>
<link rel="stylesheet" href="https://fonts.googleapis.com/css2?family=Pinyon+Script&family=Cinzel:wght@500&family=Rye&family=Amatic+SC:wght@700&display=swap">
<style>
  :root {
    --paper: #ffffff;
    --blush: #f1cdb9;
    --band: #8b8b8b;
    --band-light: #c9c9c9;
    --ink: #2a2422;
    --amber: #d08a4e;
  }
  html, body {
    margin: 0;
    padding: 0;
    width: 762px;
    height: 1200px;
    overflow: hidden;
    background: var(--paper);
  }
  .label {
    display: block;
    width: 762px;
    height: 1200px;
  }
  .frame-outer { fill: var(--paper); stroke: var(--band-light); stroke-width: 3; }
  .frame-band { fill: var(--band); }
  .frame-gap { fill: var(--blush); }
  .frame-rule { fill: var(--blush); stroke: var(--band); stroke-width: 3; }
  .farm-name {
    font-family: "Pinyon Script", cursive;
    font-size: 60px;
    fill: var(--ink);
  }
  .farm-word {
    font-family: "Cinzel", serif;
    font-size: 38px;
    letter-spacing: 4px;
    fill: var(--ink);
  }
  .product-name {
    font-family: "Rye", serif;
    fill: var(--ink);
  }
  .product-initial { font-size: 505px; }
  .product-rest { font-size: 230px; }
  .quality {
    font-family: "Rye", serif;
    font-size: 36px;
    fill: var(--ink);
  }
  .origin {
    font-family: "Amatic SC", sans-serif;
    font-weight: 700;
    font-size: 31px;
    fill: var(--ink);
  }
  .flourish-line { fill: none; stroke: var(--ink); stroke-width: 3; stroke-linecap: round; }
  .art-horse { fill: var(--ink); }
  .art-ornament { fill: var(--ink); opacity: 0.85; }
  .art-bee { fill: var(--amber); opacity: 0.75; }
</style>
</head>
<body>
<svg class="label" viewBox="0 0 762 1200" xmlns="http://www.w3.org/2000/svg">
  <defs>
    <path id="label-shape" d="M 190 16 L 572 16 Q 660 16 690 100 Q 700 150 746 170 L 746 1030 Q 700 1050 690 1100 Q 660 1184 572 1184 L 190 1184 Q 102 1184 72 1100 Q 62 1050 16 1030 L 16 170 Q 62 150 72 100 Q 102 16 190 16 Z"/>
  </defs>

  <!-- Frame layers -->
  <use href="#label-shape" class="frame-outer"/>
  <g transform="translate(381 600) scale(0.963 0.977) translate(-381 -600)">
    <use href="#label-shape" class="frame-band"/>
  </g>
  <g transform="translate(381 600) scale(0.94 0.962) translate(-381 -600)">
    <use href="#label-shape" class="frame-gap"/>
  </g>
  <g transform="translate(381 600) scale(0.92 0.949) translate(-381 -600)">
    <use href="#label-shape" class="frame-rule"/>
  </g>

  <!-- Header -->
  <rect class="art-horse" x="326" y="78" width="110" height="112" rx="10"
        role="img" aria-label="Black silhouette illustration of a standing horse"/>
  <text class="farm-name" x="381" y="248" text-anchor="middle">Marlow Brook</text>
  <text class="farm-word" x="381" y="296" text-anchor="middle">FARM</text>
  <rect class="art-ornament" x="190" y="312" width="382" height="14" rx="7"
        role="img" aria-label="Thin scrolled divider ornament with curled ends"/>

  <!-- Pointer flourish above the product name -->
  <rect class="art-ornament" x="370" y="356" width="230" height="46" rx="20"
        role="img" aria-label="Scrolled pointer flourish ornament"/>

  <!-- Product name -->
  <text class="product-name product-initial" x="72" y="768"
        textLength="288" lengthAdjust="spacingAndGlyphs">M</text>
  <text class="product-name product-rest" x="364" y="623"
        textLength="194" lengthAdjust="spacingAndGlyphs">IEL</text>

  <!-- Bee and honeycomb -->
  <rect class="art-bee" x="564" y="452" width="126" height="150" rx="18"
        role="img" aria-label="Engraved honey bee illustration over a honeycomb pattern"/>

  <!-- Finest quality with swash lines -->
  <path class="flourish-line" d="M 400 668 Q 560 618 692 628"/>
  <text class="quality" x="545" y="718" text-anchor="middle"
        textLength="280" lengthAdjust="spacingAndGlyphs"
        transform="rotate(-10 545 705)">FINEST QUALITY</text>
  <path class="flourish-line" d="M 382 772 Q 460 748 540 756"/>

  <!-- Origin -->
  <text class="origin" x="381" y="915" text-anchor="middle">Produced in Temecula Valley Wine Country, CA</text>

  <!-- Bottom ornament -->
  <rect class="art-ornament" x="228" y="950" width="306" height="140" rx="40"
        role="img" aria-label="Symmetrical floral scroll ornament"/>
</svg>
</body>
</html>
```